Kelp Pocket Apps Needs banners for webpage

We need a top banner. We are a mobile app developer for the Hospitality Industry. We are developing a Loyalty Program with the trade name KelpPerks. The banner will be used on our loyalty page inside our website.Please see www.kelppocketapps.example to understand our theme. The banner should be 1700 X 470.

Please see the attached banner. This is from a competitor website.Please use it as a model and make changes...... make it unique to KelpPocket. I need to convey the same message as this banner. Same statistics. Same setting (restaurant).

I have added a purchased vector file for the restaurant setting. I noticed many are struggling and using stock art which I don't like.Work with the background color. Make it more playful--pastels--less formal. Be creative!

Do not wait till that last day of the contest to submit. I might take the first design I like and proceed. The sooner you post a design, the better direction I can give you.
Updates

Reason: Not getting any designs I can work with yet. Please give me ideas.

All, Please re-read the brief. I have changed the banner project. It will be much easier but I need it quickly.

Now that I have made this banner much easier, I would like to wrap this contest up. Don't wait till the last day to post designs. The first design I like I will go with and close the project. Be creative, colorful, imaginative! Good luck. Martin Orrey Kelp Pocket Apps, LLC morrey@

All. See the vector file that I just purchased for the background image. Can you try different background colors. I still need the other content showing the percentages of loyalty. I do not want the rocket ship!

All, I have updated the brief. I have included a vector file that has a perfect restaurant scene. Please be creative and work with colors in this scene. Also be creative with the information in the circles showing the metrics of loyalty. Do not use the Rocket. If you find another idea to replace the rocket, that's fine. Or, just leave it off. Please make this banner unique!

Target Market(s)

Hospitality Industry.

Industry/Entity Type

Restaurant

Requirements
Must have
• Banner should be beautiful.. Image of diners at restaurant along with the statistics and message "Boost Sales".
Nice to have
• Our banner should convey the same message as the attached but we must re-design because the attached banner belongs to another company.
Should not have
• Do not re-use any of the images in the attached banner. This is from my competitor. Do not use a rocket for "Boost Sales" image.

```html
<!DOCTYPE html>
<html lang="en">
<head>
<meta charset="utf-8">
<title>Boost Sales – Loyal Guest vs. Average Guest</title>
<link rel="stylesheet" href="https://fonts.googleapis.com/css2?family=Raleway:wght@300;600;700&family=Lobster&display=swap">
<style>
  :root {
    --coral: #e65a5a;
    --coral-light: #f47474;
    --accent: #f06668;
    --frame: rgba(255, 205, 205, 0.55);
    --white: #ffffff;
    --ink: #3b3b3b;
    --grey: #6a6a6a;
    --guest-grey: #9a8f8f;
  }
  * { margin: 0; padding: 0; box-sizing: border-box; }
  html, body { width: 1200px; height: 332px; overflow: hidden; background: var(--coral); }
  .banner {
    position: relative;
    width: 1200px;
    height: 332px;
    overflow: hidden;
    font-family: "Raleway", sans-serif;
  }
  .scene {
    position: absolute;
    inset: 0;
    background: radial-gradient(ellipse at 50% 60%, var(--coral-light) 0%, #ea6262 45%, var(--coral) 100%);
  }
  .headline {
    position: absolute;
    top: 8px;
    left: 0;
    width: 100%;
    text-align: center;
    font-weight: 300;
    font-size: 64px;
    letter-spacing: 4px;
    color: var(--white);
    line-height: 1;
  }
  .subhead {
    position: absolute;
    top: 66px;
    left: 0;
    width: 100%;
    display: flex;
    justify-content: center;
    align-items: center;
    gap: 14px;
  }
  .subhead-text {
    font-family: "Lobster", cursive;
    font-size: 36px;
    color: var(--ink);
    line-height: 1;
  }
  .rule { display: block; }
  .stat-card {
    position: absolute;
    top: 160px;
    width: 266px;
    height: 150px;
    background: var(--white);
    border-radius: 4px;
    box-shadow: 0 0 0 7px var(--frame);
    text-align: center;
    color: var(--grey);
  }
  .stat-card--visits { left: 130px; }
  .stat-card--ratio { left: 466px; }
  .stat-card--spend { left: 806px; }
  .stat-label {
    position: absolute;
    left: 0;
    width: 100%;
    font-weight: 700;
    font-size: 14px;
    letter-spacing: 0.2px;
  }
  .stat-label--top { top: 18px; }
  .stat-label--bottom { bottom: 14px; }
  .stat-value {
    position: absolute;
    top: 36px;
    left: 0;
    width: 100%;
    font-family: "Lobster", cursive;
    font-size: 88px;
    line-height: 1;
    color: var(--accent);
    text-shadow: 2px 2px 0 rgba(240, 102, 104, 0.25);
  }
  .ratio-graphic { position: absolute; top: 10px; left: 20px; }
  .ratio-caption {
    position: absolute;
    bottom: 12px;
    left: 0;
    width: 100%;
    font-weight: 700;
    font-size: 12px;
  }
  .ratio-caption .num {
    font-family: "Lobster", cursive;
    font-weight: 400;
    font-size: 17px;
    color: var(--accent);
  }
</style>
</head>
<body>
  <div class="banner">
    <div class="scene" role="img" aria-label="Restaurant scene with silhouettes of diners, waiters and wine glasses in coral tones"></div>

    <h1 class="headline">BOOST SALES</h1>
    <div class="subhead">
      <svg class="rule" width="50" height="8" viewBox="0 0 50 8"><line x1="0" y1="4" x2="44" y2="4" stroke="#3b3b3b" stroke-width="1.5"/><circle cx="46" cy="4" r="3" fill="#3b3b3b"/></svg>
      <span class="subhead-text">Loyal Guest vs. Average Guest</span>
      <svg class="rule" width="50" height="8" viewBox="0 0 50 8"><circle cx="4" cy="4" r="3" fill="#3b3b3b"/><line x1="6" y1="4" x2="50" y2="4" stroke="#3b3b3b" stroke-width="1.5"/></svg>
    </div>

    <section class="stat-card stat-card--visits">
      <p class="stat-label stat-label--top">LOYAL GUESTS VISIT ABOUT</p>
      <p class="stat-value">32%</p>
      <p class="stat-label stat-label--bottom">MORE THAN AVERAGE GUESTS</p>
    </section>

    <section class="stat-card stat-card--ratio">
      <svg class="ratio-graphic" width="230" height="112" viewBox="0 0 230 112" aria-hidden="true">
        <defs>
          <g id="guest-icon">
            <circle cx="10" cy="5" r="5"/>
            <rect x="2" y="11" width="16" height="16" rx="3"/>
            <rect x="4" y="24" width="5" height="20" rx="1"/>
            <rect x="11" y="24" width="5" height="20" rx="1"/>
          </g>
        </defs>
        <g fill="#f06668" transform="translate(-6,2) scale(2.45)">
          <use href="#guest-icon"/>
        </g>
        <rect x="78" y="52" width="18" height="3" fill="#f06668"/>
        <rect x="78" y="60" width="18" height="3" fill="#f06668"/>
        <g fill="#9a8f8f">
          <use href="#guest-icon" transform="translate(110,4)"/>
          <use href="#guest-icon" transform="translate(134,4)"/>
          <use href="#guest-icon" transform="translate(158,4)"/>
          <use href="#guest-icon" transform="translate(182,4)"/>
          <use href="#guest-icon" transform="translate(206,4)"/>
          <use href="#guest-icon" transform="translate(110,56)"/>
          <use href="#guest-icon" transform="translate(134,56)"/>
          <use href="#guest-icon" transform="translate(158,56)"/>
          <use href="#guest-icon" transform="translate(182,56)"/>
          <use href="#guest-icon" transform="translate(206,56)"/>
        </g>
      </svg>
      <p class="ratio-caption"><span class="num">1</span> LOYAL GUEST = <span class="num">10</span> AVERAGE GUESTS</p>
    </section>

    <section class="stat-card stat-card--spend">
      <p class="stat-label stat-label--top">LOYAL GUESTS SPEND ABOUT</p>
      <p class="stat-value">22%</p>
      <p class="stat-label stat-label--bottom">MORE THAN AVERAGE GUESTS</p>
    </section>
  </div>
</body>
</html>
```